Bright Mesh Business Card

This is a business card for a printing company but I actually don't have a logo. Just need to typeset the words "Bright Mesh Printing" as the logo. Then add my name "Loretta Vance" + phone number + address

Target Market(s)

ceos and professionals

Industry/Entity Type

printing and manufacturing

Contact Information for Business Card

Bright Mesh Printing/ 4617 calloway st. Alder Grove, OR 91648/ 626-417-3980/ Loretta Vance

Font styles to use
Serif
Other font styles liked:
• a modern font would be nice

Colors
0054AA
0677BA
7BADD7
CADEEF
E8F1F8
0094D4
00A9DD
6FCCEA
C7EBF8
E9F6FB

Requirements
Must have
• company name, number, address
Nice to have
• nice bold feel
Should not have
• nothing in particular

```html
<!DOCTYPE html>
<html lang="en">
<head>
<meta charset="utf-8">
<title>Bright Mesh Printing – Business Card</title>
<link rel="stylesheet" href="https://fonts.googleapis.com/css2?family=Montserrat:wght@500;700;800&family=Open+Sans:wght@400&display=swap">
<style>
  :root {
    --brand-blue: #0054AA;
    --mid-blue: #0677BA;
    --sky-blue: #7BADD7;
    --pale-blue: #CADEEF;
    --card-white: #F7F8F9;
    --ink: #1E2430;
    --muted: #6A707A;
    --backdrop: #E4E5E7;
  }
  * { box-sizing: border-box; margin: 0; padding: 0; }
  html, body { width: 1200px; height: 675px; overflow: hidden; }
  body {
    background: var(--backdrop);
    position: relative;
    font-family: "Open Sans", Arial, sans-serif;
  }
  .card {
    position: absolute;
    top: 195px;
    width: 500px;
    height: 286px;
    border-radius: 16px;
    overflow: hidden;
    box-shadow: 0 6px 18px rgba(0,0,0,0.12);
  }
  /* Front side */
  .card-front { left: 60px; background: var(--card-white); }
  .front-wordmark {
    position: absolute;
    left: 36px;
    top: 34px;
    width: 300px;
    font-family: "Montserrat", Arial, sans-serif;
    font-weight: 800;
    font-size: 38px;
    line-height: 1.02;
    letter-spacing: -0.5px;
    text-transform: uppercase;
    color: var(--brand-blue);
  }
  .accent-band {
    position: absolute;
    left: 370px;
    top: 0;
    width: 40px;
    height: 150px;
    background: var(--pale-blue);
    border-radius: 0 0 6px 6px;
  }
  .holder-name {
    position: absolute;
    right: 40px;
    top: 164px;
    font-family: "Montserrat", Arial, sans-serif;
    font-weight: 700;
    font-size: 24px;
    line-height: 1.1;
    color: var(--brand-blue);
  }
  .divider {
    position: absolute;
    left: 32px;
    right: 40px;
    top: 200px;
    height: 1.5px;
    background: var(--brand-blue);
  }
  .holder-role {
    position: absolute;
    right: 40px;
    top: 205px;
    font-family: "Montserrat", Arial, sans-serif;
    font-weight: 500;
    font-size: 10px;
    letter-spacing: 1px;
    color: var(--muted);
  }
  .contact {
    position: absolute;
    left: 52px;
    top: 216px;
    list-style: none;
    font-size: 14px;
    color: var(--ink);
  }
  .contact li { display: flex; align-items: center; gap: 10px; margin-bottom: 6px; }
  .contact li.phone { padding-left: 80px; }
  .contact svg { width: 15px; height: 15px; flex: none; }

  /* Back side */
  .card-back {
    left: 640px;
    background: linear-gradient(135deg, var(--brand-blue), #1466B6);
  }
  .back-band {
    position: absolute;
    right: 0;
    top: 178px;
    width: 120px;
    height: 44px;
    background: var(--mid-blue);
    opacity: 0.8;
  }
  .back-wordmark {
    position: absolute;
    left: 0;
    right: 0;
    top: 50%;
    transform: translateY(-50%);
    text-align: center;
    font-family: "Montserrat", Arial, sans-serif;
    font-weight: 800;
    font-size: 38px;
    line-height: 1.02;
    letter-spacing: -0.5px;
    text-transform: uppercase;
    color: #FFFFFF;
  }
</style>
</head>
<body>
  <section class="card card-front" aria-label="Business card front">
    <div class="accent-band"></div>
    <h1 class="front-wordmark">Bright Mesh Printing</h1>
    <p class="holder-name">Loretta Vance</p>
    <div class="divider"></div>
    <p class="holder-role">OWNER</p>
    <ul class="contact">
      <li class="address">
        <svg viewBox="0 0 24 24" aria-hidden="true"><path fill="#0054AA" d="M12 2a7 7 0 0 0-7 7c0 5 7 12 7 12s7-7 7-12a7 7 0 0 0-7-7zm0 9.5A2.5 2.5 0 1 1 12 6.5a2.5 2.5 0 0 1 0 5z"/></svg>
        4617 Calloway St. Alder Grove, OR 91648
      </li>
      <li class="phone">
        <svg viewBox="0 0 24 24" aria-hidden="true"><path fill="#0054AA" d="M6.6 10.8a15 15 0 0 0 6.6 6.6l2.2-2.2a1 1 0 0 1 1-.25 11.4 11.4 0 0 0 3.6.57 1 1 0 0 1 1 1V20a1 1 0 0 1-1 1A17 17 0 0 1 3 4a1 1 0 0 1 1-1h3.5a1 1 0 0 1 1 1c0 1.25.2 2.45.57 3.57a1 1 0 0 1-.25 1z"/></svg>
        626-417-3980
      </li>
    </ul>
  </section>

  <section class="card card-back" aria-label="Business card back">
    <div class="back-band"></div>
    <p class="back-wordmark">Bright Mesh<br>Printing</p>
  </section>
</body>
</html>
```